Stationery modern simple design
Corporate Stationery
Project: Stationery modern simple design
Creative Brief
Simple
Faisal Alqurashi
General Manager
Sable Grid Company 3858 Nakheel Crest Rd Wardah Tower Riyadh 13847 Saudi Arabia
info@sablegrid.example
www.sablegrid.example
address will be not use in business card and will be used in any other Stationery Arabic Address: شركة سابل جريد ٣٨٥٨ طريق النخيل الأعلى الرياض ١٣٨٤٧ المملكة العربية السعودية
فيصل القرشي المدير العام infor@sablegrid.example +966117290813 +9665031476095

```html
<!DOCTYPE html>
<html lang="en">
<head>
<meta charset="UTF-8">
<title>Sable Grid — Business Card</title>
<link href="https://fonts.googleapis.com/css2?family=Roboto+Slab:wght@400;700&family=Montserrat:wght@500&display=swap" rel="stylesheet">
<style>
  :root {
    --stage: #2a2c2f;
    --card-dark: #2e3236;
    --card-dark-edge: #3a3f44;
    --card-light: #ffffff;
    --brand-blue: #1c8fd8;
    --ink: #4a4f55;
    --ink-soft: #7a8088;
    --rule: #c9ced3;
    --stripe-dark: #3a3f45;
  }
  * { margin: 0; padding: 0; box-sizing: border-box; }
  html, body { width: 1200px; height: 871px; overflow: hidden; }
  body {
    background: var(--stage);
    position: relative;
    font-family: "Roboto Slab", Georgia, serif;
  }
  .card {
    position: absolute;
    width: 520px;
    height: 300px;
    border-radius: 3px;
    overflow: hidden;
    box-shadow: 0 18px 40px rgba(0,0,0,0.45);
  }

  /* Back of card */
  .card--back {
    left: 60px;
    top: 170px;
    background: var(--card-dark);
  }
  .card--back .pattern-field {
    position: absolute;
    left: 0; top: 0;
    width: 300px; height: 300px;
    background: linear-gradient(100deg, #8d949b 0%, #5b6268 40%, rgba(46,50,54,0) 100%);
    opacity: 0.55;
  }
  .card--back .back-brand {
    position: absolute;
    left: 320px;
    top: 108px;
    display: flex;
    align-items: center;
    gap: 8px;
    font-family: "Montserrat", Arial, sans-serif;
    font-weight: 500;
    font-size: 17px;
    letter-spacing: 1px;
    color: var(--brand-blue);
    text-transform: uppercase;
  }
  .brand-square {
    width: 12px; height: 12px;
    background: var(--brand-blue);
  }

  /* Front of card */
  .card--front {
    left: 620px;
    top: 400px;
    background: var(--card-light);
  }
  .front-brand {
    position: absolute;
    left: 36px;
    top: 128px;
    display: flex;
    align-items: center;
    gap: 12px;
    font-family: "Montserrat", Arial, sans-serif;
    font-weight: 500;
    font-size: 30px;
    letter-spacing: 1px;
    color: var(--ink);
    text-transform: uppercase;
  }
  .front-brand .brand-square { width: 18px; height: 18px; }
  .divider {
    position: absolute;
    left: 268px;
    top: 38px;
    width: 1px;
    height: 200px;
    background: var(--rule);
  }
  .contact {
    position: absolute;
    left: 284px;
    top: 34px;
    color: var(--ink);
  }
  .contact__name {
    font-weight: 700;
    font-size: 19px;
    color: var(--brand-blue);
    line-height: 1.1;
  }
  .contact__title {
    font-size: 10px;
    color: var(--ink-soft);
    margin-top: 2px;
  }
  .contact__address {
    font-size: 10.5px;
    line-height: 1.45;
    margin-top: 16px;
    color: var(--ink-soft);
  }
  .contact__list {
    list-style: none;
    margin-top: 14px;
    font-size: 10.5px;
    line-height: 1.65;
    color: var(--ink-soft);
  }
  .contact__list li { display: flex; align-items: center; gap: 7px; }
  .contact__list svg { width: 9px; height: 9px; flex: none; }
  .corner-stripes {
    position: absolute;
    right: 0; bottom: 0;
    width: 520px; height: 300px;
  }
</style>
</head>
<body>

  <section class="card card--back" aria-label="Card back">
    <div class="pattern-field" role="img" aria-label="Repeating brand-mark pattern in silver foil fading across the dark card"></div>
    <div class="back-brand"><span class="brand-square"></span>Sable Grid</div>
  </section>

  <section class="card card--front" aria-label="Card front">
    <div class="front-brand"><span class="brand-square"></span>Sable Grid</div>
    <div class="divider"></div>

    <div class="contact">
      <p class="contact__name">Faisal Alqurashi</p>
      <p class="contact__title">General Manager</p>
      <p class="contact__address">
        Sable Grid Company<br>
        3858 Nakheel Crest Rd Wardah Tower<br>
        Riyadh 13847 Saudi Arabia
      </p>
      <ul class="contact__list">
        <li>
          <svg viewBox="0 0 10 10"><path d="M2 1 L4 1 L4.6 3 L3.4 3.8 Q4.4 5.8 6.2 6.6 L7 5.4 L9 6 L9 8 Q5 9.5 1.5 5 Q0.6 2.6 2 1 Z" fill="var(--brand-blue)"/></svg>
          +966117290813
        </li>
        <li>
          <svg viewBox="0 0 10 10"><rect x="2.5" y="0.5" width="5" height="9" rx="1" fill="var(--brand-blue)"/><rect x="3.5" y="1.8" width="3" height="5.5" fill="#fff"/></svg>
          +9665031476095
        </li>
        <li>
          <svg viewBox="0 0 10 10"><rect x="0.5" y="2" width="9" height="6" rx="0.8" fill="var(--brand-blue)"/><path d="M0.8 2.4 L5 5.6 L9.2 2.4" stroke="#fff" stroke-width="0.8" fill="none"/></svg>
          info@sablegrid.example
        </li>
        <li>
          <svg viewBox="0 0 10 10"><circle cx="5" cy="5" r="4.5" fill="var(--brand-blue)"/><path d="M0.6 5 H9.4 M5 0.6 Q2.4 5 5 9.4 M5 0.6 Q7.6 5 5 9.4" stroke="#fff" stroke-width="0.7" fill="none"/></svg>
          www.sablegrid.example
        </li>
      </ul>
    </div>

    <svg class="corner-stripes" viewBox="0 0 520 300" aria-hidden="true">
      <polygon points="300,300 520,300 520,270 330,290" fill="var(--stripe-dark)"/>
      <polygon points="400,284 520,266 520,276 410,290" fill="var(--brand-blue)"/>
    </svg>
  </section>

</body>
</html>
```